KVR GUARDING WEBSITE BANNER DESIGN OF AWESOME

Please take a look at the attached Banner. I want a redesign Idea. The requirements are below.

1)Must Use Website Background
2)Must Use Photo Provided
3)Must Include Button
4)Website the banner will be used on you can see the current at the bottom of the page: https://b.pelmarox.com

Target Market(s)

Anyone Seeking Security Guard Services

```html
<!DOCTYPE html>
<html lang="en">
<head>
<meta charset="UTF-8">
<title>Get Secured Today – Banner</title>
<link rel="stylesheet" href="https://fonts.googleapis.com/css2?family=Nunito:wght@500;600&family=Arimo:wght@700&display=swap">
<style>
  :root {
    --navy-deep: #173a63;
    --navy: #1b4a7a;
    --navy-light: #235a8e;
    --white: #ffffff;
    --amber: #f6a81a;
    --ink: #10253f;
    --photo-dark: #141c2a;
    --photo-mid: #2a3c58;
    --photo-light: #6f89b4;
  }
  * { margin: 0; padding: 0; box-sizing: border-box; }
  html, body { width: 1200px; height: 205px; overflow: hidden; background: var(--navy-deep); }
  .banner {
    position: relative;
    width: 1200px;
    height: 205px;
    overflow: hidden;
    background: linear-gradient(100deg, var(--navy-deep) 0%, var(--navy) 45%, var(--navy-light) 75%, var(--navy) 100%);
    font-family: "Nunito", sans-serif;
  }
  .facets { position: absolute; inset: 0; width: 1200px; height: 205px; }
  .photo {
    position: absolute;
    inset: 0;
    width: 1200px;
    height: 205px;
  }
  .headline {
    position: absolute;
    left: 104px;
    top: 12px;
    font-family: "Nunito", sans-serif;
    font-weight: 600;
    font-size: 71px;
    line-height: 1.2;
    letter-spacing: 0.5px;
    color: var(--white);
    white-space: nowrap;
  }
  .tagline {
    position: absolute;
    left: 124px;
    top: 96px;
    font-family: "Arimo", sans-serif;
    font-weight: 700;
    font-size: 40px;
    line-height: 1.1;
    color: var(--amber);
    white-space: nowrap;
  }
  .features {
    position: absolute;
    left: 124px;
    top: 163px;
    display: flex;
    list-style: none;
    gap: 26px;
    color: var(--white);
    font-size: 15.5px;
    font-weight: 500;
    letter-spacing: 0.6px;
    white-space: nowrap;
  }
  .features li { display: flex; align-items: center; gap: 3px; }
  .features svg { width: 17px; height: 17px; }
  .cta {
    position: absolute;
    left: 611px;
    top: 160px;
    width: 124px;
    height: 28px;
    border-radius: 8px;
    background: var(--amber);
    color: var(--ink);
    font-size: 15px;
    font-weight: 500;
    letter-spacing: 0.5px;
    display: flex;
    align-items: center;
    justify-content: center;
    text-decoration: none;
    box-shadow: 0 2px 5px rgba(0,0,0,0.3);
  }
</style>
</head>
<body>
<div class="banner">
  <svg class="facets" viewBox="0 0 1200 205" aria-hidden="true">
    <polygon points="0,0 560,0 150,205 0,205" fill="#ffffff" opacity="0.025"/>
    <polygon points="560,0 900,0 700,205 300,205" fill="#ffffff" opacity="0.035"/>
    <polygon points="150,0 420,0 60,205 0,205" fill="#000000" opacity="0.04"/>
  </svg>

  <svg class="photo" viewBox="0 0 1200 205" role="img" aria-label="Photo of a security guard in a dark uniform shining a flashlight up a stairwell at night">
    <defs>
      <linearGradient id="photoFill" x1="0" y1="1" x2="1" y2="0">
        <stop offset="0" stop-color="var(--photo-dark)"/>
        <stop offset="0.5" stop-color="var(--photo-mid)"/>
        <stop offset="1" stop-color="var(--photo-light)"/>
      </linearGradient>
    </defs>
    <polygon points="866,0 1200,0 1200,205 778,205" fill="url(#photoFill)"/>
  </svg>

  <h1 class="headline">Get Secured Today</h1>
  <p class="tagline">We take your security personal.</p>

  <ul class="features">
    <li>
      <svg viewBox="0 0 18 18" aria-hidden="true"><rect x="1.5" y="3.5" width="13" height="13" fill="none" stroke="var(--amber)" stroke-width="1.8"/><path d="M5 9.5l3 3 8.5-11" fill="none" stroke="var(--amber)" stroke-width="2"/></svg>
      Client Portal
    </li>
    <li>
      <svg viewBox="0 0 18 18" aria-hidden="true"><rect x="1.5" y="3.5" width="13" height="13" fill="none" stroke="var(--amber)" stroke-width="1.8"/><path d="M5 9.5l3 3 8.5-11" fill="none" stroke="var(--amber)" stroke-width="2"/></svg>
      24x7 Dispatch
    </li>
    <li>
      <svg viewBox="0 0 18 18" aria-hidden="true"><rect x="1.5" y="3.5" width="13" height="13" fill="none" stroke="var(--amber)" stroke-width="1.8"/><path d="M5 9.5l3 3 8.5-11" fill="none" stroke="var(--amber)" stroke-width="2"/></svg>
      No Binding Contracts
    </li>
  </ul>

  <a class="cta" href="#">GET STARTED</a>
</div>
</body>
</html>
```